Business Card: RW Office Partners - Your tidy answer finder

Business Name: RW Office Partners
Website: www.rwofficepartners.com.au
Email: marisol@rwofficepartners.com.au
Mobile: 61 487 902 346
Facebook: @rwofficepartners
Instrgram: @rwofficepartners

Brading Colours:
HEX
#986474
#ddccd3
#7a8498
#c9d8e4
#000000
#ffffff

Tag Line: Your organised problem solver

Link to DRAFT website:
https://helpdeskhub.sitebuilderx.com/rw-office-partners

About Page from the website:
My name is Marisol Bramwell, and I would love to assist you to become more productive in your day to day and achieve your business and personal goals.
My mission is to give you time, time to work on the important tasks of your business or to be able to spend more time with your family. I will take on the tasks you don’t have time for, don’t know well or simply don’t like to do.
I have an extensive background in Administration, Tender Coordination, Document Control, WHS and Quality Management working primarily in the Construction, Mining and Corporate World.
I am passionate about being organised, having order and making things in your life (and mine) easier! I love to watch something unfold and grow into something amazing! I am known for being the go-to problem solver, the organiser of all things, producing high standards of work even under pressure. I’m also a confident communicator, and I understand that you’re busy running your business.

Target Market(s)

Small to Medium Business who require assistance in their business by a virtual assistant.

Industry/Entity Type

Virtual Assistant

Contact Information for Business Card

Mobile: 61 487 902 346

Font styles to use
Sans Serif

Colors
ffffff

Requirements
Must have
• Branding Colours as outlined.
Contact Details as outlined.
Logo as provided.
Proper contact details - mobile, facebook, instragm, website.
Simple, Elegant, very clean looking.
Should not have
• Note cute with pictures.
Not too girly as still want to market to construction companies.

```html
<!DOCTYPE html>
<html lang="en">
<head>
<meta charset="utf-8">
<title>RW Office Partners – Business Card</title>
<link rel="stylesheet" href="https://fonts.googleapis.com/css2?family=Montserrat:wght@500;600&family=Roboto:wght@400;700&display=swap">
<style>
  :root {
    --brand-rose: #986474;
    --brand-blush: #ddccd3;
    --brand-slate: #7a8498;
    --brand-mist: #c9d8e4;
    --ink: #000000;
    --paper: #ffffff;
    --backdrop: #e4e4e8;
    --text-dark: #2b2b2e;
  }
  * { box-sizing: border-box; margin: 0; padding: 0; }
  html, body {
    width: 1200px;
    height: 675px;
    overflow: hidden;
    background: var(--backdrop);
  }
  .canvas {
    position: relative;
    width: 1200px;
    height: 675px;
    display: flex;
    align-items: center;
    justify-content: center;
    gap: 60px;
  }
  .card {
    position: relative;
    width: 525px;
    height: 300px;
    box-shadow: 0 10px 28px rgba(0,0,0,0.16);
    overflow: hidden;
  }

  /* Front */
  .card--front {
    background: var(--ink);
    display: flex;
    flex-direction: column;
    align-items: center;
    justify-content: center;
  }
  .wordmark {
    font-family: "Montserrat", sans-serif;
    font-weight: 600;
    text-transform: uppercase;
    color: var(--brand-slate);
    letter-spacing: 0.04em;
    line-height: 1;
  }
  .card--front .wordmark {
    font-size: 32px;
    text-align: center;
  }
  .tagline {
    margin-top: 54px;
    font-family: "Montserrat", sans-serif;
    font-weight: 500;
    font-size: 12px;
    letter-spacing: 0.32em;
    text-transform: uppercase;
    color: var(--brand-rose);
  }

  /* Back */
  .card--back {
    background: var(--paper);
    display: flex;
    align-items: center;
    padding: 0 24px 24px 30px;
  }
  .card--back .wordmark {
    font-size: 19px;
    width: 170px;
    flex: none;
    line-height: 1.18;
    margin-top: 40px;
  }
  .divider {
    width: 1.5px;
    height: 130px;
    flex: none;
    background: var(--brand-rose);
    margin: 0 18px 0 8px;
  }
  .contact {
    font-family: "Roboto", sans-serif;
    color: var(--text-dark);
    min-width: 0;
  }
  .contact__name {
    font-weight: 700;
    font-size: 20px;
    color: var(--brand-rose);
    white-space: nowrap;
  }
  .contact__role {
    font-size: 13px;
    margin-bottom: 12px;
  }
  .contact__list { list-style: none; }
  .contact__item {
    display: flex;
    align-items: center;
    gap: 8px;
    font-size: 13px;
    line-height: 1.6;
    white-space: nowrap;
  }
  .contact__icon {
    width: 13px;
    height: 13px;
    flex: none;
    fill: var(--brand-rose);
  }
  .contact__social-square {
    width: 12px;
    height: 12px;
    background: var(--brand-rose);
    border-radius: 2px;
    flex: none;
    margin-right: 1px;
  }
  .edge-band {
    position: absolute;
    left: 0;
    right: 0;
    bottom: 0;
    height: 14px;
    background: var(--brand-rose);
  }
</style>
</head>
<body>
<main class="canvas">
  <section class="card card--front" aria-label="Card front">
    <p class="wordmark">RW Office Partners</p>
    <p class="tagline">Your tidy answer finder</p>
  </section>

  <section class="card card--back" aria-label="Card back">
    <p class="wordmark">RW Office Partners</p>
    <span class="divider" aria-hidden="true"></span>
    <div class="contact">
      <p class="contact__name">Marisol Bramwell</p>
      <p class="contact__role">Director</p>
      <ul class="contact__list">
        <li class="contact__item">
          <svg class="contact__icon" viewBox="0 0 16 16" aria-hidden="true"><path d="M4 0h8a1.5 1.5 0 0 1 1.5 1.5v13A1.5 1.5 0 0 1 12 16H4a1.5 1.5 0 0 1-1.5-1.5v-13A1.5 1.5 0 0 1 4 0zm0.5 2v10.5h7V2zM8 13.4a.9.9 0 1 0 0 1.8.9.9 0 0 0 0-1.8z"/></svg>
          61 487 902 346
        </li>
        <li class="contact__item">
          <svg class="contact__icon" viewBox="0 0 16 16" aria-hidden="true"><path d="M0 3h16v10H0zm1.5 1.2v.3L8 9l6.5-4.5v-.3zm0 2.1V11.8h13V6.3L8 10.8z"/></svg>
          marisol@rwofficepartners.com.au
        </li>
        <li class="contact__item">
          <svg class="contact__icon" viewBox="0 0 16 16" aria-hidden="true"><circle cx="8" cy="8" r="7.5"/><path d="M1 8h14M8 .5c-2.5 3-2.5 12 0 15M8 .5c2.5 3 2.5 12 0 15" stroke="#fff" stroke-width="1" fill="none"/></svg>
          www.rwofficepartners.com.au
        </li>
        <li class="contact__item">
          <span class="contact__social-square" aria-hidden="true"></span>
          @rwofficepartners
        </li>
      </ul>
    </div>
    <span class="edge-band" aria-hidden="true"></span>
  </section>
</main>
</body>
</html>
```